Post card

I want an educational customer postcard with our logo, email, and contact number. We are a residential foundation inspection & repair company here in Los Angeles. We provide foundation repair, earthquake retrofitting, and reinforcement.
Our number is 323-555-0148.
Email info@bramblecrestworks.com
Our license number is #2839165

OUR GOAL
Our primary objective is to empower clients with comprehensive knowledge about foundation issues and earthquake retrofitting. By educating them on the potential risks associated with foundation problems and the importance of earthquake retrofitting, we aim to equip homeowners with the necessary information to make informed decisions about safeguarding their properties. Highlighting the benefits of having their houses properly bolted not only enhances structural integrity but also provides peace of mind during seismic events, ensuring the safety and security of their homes and loved ones.

```html
<!DOCTYPE html>
<html lang="en">
<head>
<meta charset="utf-8">
<title>Bramblecrest Works – Residential Seismic Retrofit Postcard</title>
<link href="https://fonts.googleapis.com/css2?family=Montserrat:wght@400;500;600;700;800;900&display=swap" rel="stylesheet">
<style>
  :root {
    --blue: #0a63f5;
    --brand-blue: #0b5fe0;
    --red: #d0101f;
    --ink: #111111;
    --band: #e6e6e6;
    --paper: #ffffff;
    --page: #f3f3f3;
    --rule: #9a9a9a;
    --stamp: #f1f1f1;
  }
  * { margin: 0; padding: 0; box-sizing: border-box; }
  html, body { width: 673px; height: 1200px; overflow: hidden; }
  body { background: var(--page); font-family: "Montserrat", sans-serif; position: relative; }

  .card {
    position: absolute; left: 26px; width: 620px; height: 413px;
    background: var(--paper); overflow: hidden;
    box-shadow: 0 10px 30px rgba(0,0,0,0.12);
  }
  .card--front { top: 150px; }
  .card--back { top: 620px; }

  .brand { position: absolute; display: flex; align-items: center; gap: 7px; }
  .brand__mark { background: var(--brand-blue); flex: none; }
  .brand__name { font-weight: 800; color: var(--brand-blue); line-height: 1.05; letter-spacing: 0.2px; font-family: "Montserrat", sans-serif; }
  .brand__license { position: absolute; font-weight: 700; color: var(--ink); text-align: right; }

  .front__brand { left: 39px; top: 22px; }
  .front__brand .brand__mark { width: 26px; height: 26px; }
  .front__brand .brand__name { font-size: 18px; }
  .front__license { left: 130px; width: 60px; top: 64px; font-size: 5px; }

  .headline { position: absolute; left: 31px; top: 95px; font-weight: 900; line-height: 1; white-space: nowrap; }
  .headline__line { display: block; font-size: 30px; letter-spacing: -0.5px; margin-bottom: 6px; }
  .headline__line--blue { color: var(--blue); }
  .headline__line--red { color: var(--red); font-size: 35px; margin-bottom: 4px; }

  .service-area { position: absolute; left: 33px; top: 214px; font-weight: 800; font-size: 14px; line-height: 1.45; color: var(--ink); }

  .hero-photo {
    position: absolute; left: 279px; top: 0; width: 341px; height: 281px;
    background: linear-gradient(180deg, #2a62b8 0%, #3f74bd 35%, #8a6a4a 55%, #c98f52 63%, #2f3a2a 80%, #1f2a1c 100%);
  }

  .goal-band { position: absolute; left: 0; top: 281px; width: 620px; height: 80px; background: var(--band); }
  .goal-band__title { position: absolute; left: 39px; top: 5px; font-size: 16px; font-weight: 800; color: var(--blue); }
  .goal-band__text { position: absolute; left: 40px; top: 26px; width: 520px; font-size: 6.2px; line-height: 1.4; color: var(--ink); }

  .contact-bar {
    position: absolute; left: 0; bottom: 0; width: 620px; background: var(--blue);
    display: flex; align-items: center; justify-content: center; gap: 13px;
    color: #fff; font-weight: 600; font-size: 13.5px;
  }
  .card--front .contact-bar { height: 52px; }
  .card--back .contact-bar { height: 43px; }
  .contact-bar__item { display: flex; align-items: center; gap: 5px; white-space: nowrap; }
  .contact-bar__icon { width: 13px; height: 13px; }

  .services__title { position: absolute; left: 81px; top: 18px; font-size: 20px; font-weight: 800; color: var(--red); }
  .service { position: absolute; width: 120px; }
  .service__photo { height: 51px; }
  .service__label {
    background: var(--red); color: #fff; font-size: 9px; text-align: center;
    line-height: 1.25; padding: 1.5px 0; margin: 1px 1px 0;
  }

  .back__brand { left: 359px; top: 70px; gap: 5px; }
  .back__brand .brand__mark { width: 16px; height: 16px; }
  .back__brand .brand__name { font-size: 10.5px; }
  .back__license { left: 420px; width: 51px; top: 96px; font-size: 4px; }
  .stamp-box { position: absolute; left: 503px; top: 51px; width: 60px; height: 60px; background: var(--stamp); }
  .address-line { position: absolute; left: 356px; width: 198px; height: 1px; background: var(--rule); }
</style>
</head>
<body>

<section class="card card--front">
  <div class="brand front__brand">
    <span class="brand__mark"></span>
    <span class="brand__name">BRAMBLECREST<br>WORKS</span>
  </div>
  <span class="brand__license front__license">#2839165</span>

  <h1 class="headline">
    <span class="headline__line headline__line--blue">RESIDENTIAL</span>
    <span class="headline__line headline__line--red">SEISMIC</span>
    <span class="headline__line headline__line--red">RETROFIT</span>
  </h1>
  <p class="service-area">SERVICING LOS ANGELES &amp;<br>SURROUNDING CITIES</p>

  <div class="hero-photo" role="img" aria-label="Modern two-storey home at dusk with glowing windows and a lawn"></div>

  <div class="goal-band">
    <h2 class="goal-band__title">OUR GOAL</h2>
    <p class="goal-band__text">Our primary objective is to empower clients with comprehensive knowledge about foundation issues and earthquake retrofitting. By educating them on the potential risks associated with foundation problems and the importance of earthquake retrofitting, we aim to equip homeowners with the necessary information to make informed decisions about safeguarding their properties. Highlighting the benefits of having their houses properly bolted not only enhances structural integrity but also provides peace of mind during seismic events, ensuring the safety and security of their homes and loved ones.</p>
  </div>

  <div class="contact-bar">
    <span class="contact-bar__item">
      <svg class="contact-bar__icon" viewBox="0 0 24 24" fill="none" stroke="#fff" stroke-width="1.8"><path d="M5 3h4l2 5-2.5 1.5a11 11 0 0 0 6 6L16 13l5 2v4a2 2 0 0 1-2 2A17 17 0 0 1 3 5a2 2 0 0 1 2-2z"/></svg>
      (323) 555 0148
    </span>
    <span class="contact-bar__item">
      <svg class="contact-bar__icon" viewBox="0 0 24 24" fill="none" stroke="#fff" stroke-width="1.6"><circle cx="12" cy="12" r="10"/><ellipse cx="12" cy="12" rx="4.5" ry="10"/><path d="M2 12h20M4 7h16M4 17h16"/></svg>
      www.bramblecrestworks.com
    </span>
    <span class="contact-bar__item">
      <svg class="contact-bar__icon" viewBox="0 0 24 24" fill="none" stroke="#fff" stroke-width="1.6"><rect x="2" y="5" width="20" height="14"/><path d="M2 5l10 8 10-8"/></svg>
      info@bramblecrestworks.com
    </span>
  </div>
</section>

<section class="card card--back">
  <h2 class="services__title">OUR SERVICES</h2>

  <div class="service" style="left:38px; top:47px;">
    <div class="service__photo" role="img" aria-label="Inspector's light in a dark crawl space" style="background:linear-gradient(180deg,#6b6b6b,#262626 60%,#3b3b3b);"></div>
    <div class="service__label">Foundation Inspections</div>
  </div>
  <div class="service" style="left:173px; top:47px;">
    <div class="service__photo" role="img" aria-label="Steel anchor plates bolting a mudsill to the foundation" style="background:linear-gradient(180deg,#8a7a68,#b3b3b3 50%,#7d7d7d);"></div>
    <div class="service__label">House Bolting</div>
  </div>
  <div class="service" style="left:38px; top:120px;">
    <div class="service__photo" role="img" aria-label="Metal plate bolted across a foundation crack" style="background:linear-gradient(180deg,#4e4e4e,#8d8d8d 55%,#5c5c5c);"></div>
    <div class="service__label">Crack Repair</div>
  </div>
  <div class="service" style="left:173px; top:120px;">
    <div class="service__photo" role="img" aria-label="Reinforced wooden beam with steel brackets" style="background:linear-gradient(180deg,#6e5a45,#2b2b2b 45%,#8a7358);"></div>
    <div class="service__label">Beam Reinforcment</div>
  </div>
  <div class="service" style="left:38px; top:194px;">
    <div class="service__photo" role="img" aria-label="Cracked concrete foundation wall under floor joists" style="background:linear-gradient(180deg,#7a7a7a,#a19f99 50%,#4a4a4a);"></div>
    <div class="service__label">Structural Defects</div>
  </div>
  <div class="service" style="left:173px; top:194px;">
    <div class="service__photo" role="img" aria-label="Plywood cripple wall bracing with vent holes" style="background:linear-gradient(180deg,#5a4a36,#c89a55 45%,#8c6a3d);"></div>
    <div class="service__label">Cripple Wall Bracing</div>
  </div>
  <div class="service" style="left:38px; top:271px;">
    <div class="service__photo" role="img" aria-label="Stitched crack in a concrete slab" style="background:linear-gradient(180deg,#6f6f6f,#9a9a9a 60%,#7c7c7c);"></div>
    <div class="service__label">Foundation<br>Crack Stitching</div>
  </div>
  <div class="service" style="left:173px; top:271px;">
    <div class="service__photo" role="img" aria-label="Crawl space lined with white vapour barrier" style="background:linear-gradient(180deg,#5a4632,#b48a5a 40%,#e3e3e3);"></div>
    <div class="service__label">Crawl Space<br>Encapsulation</div>
  </div>

  <div class="brand back__brand">
    <span class="brand__mark"></span>
    <span class="brand__name">BRAMBLECREST<br>WORKS</span>
  </div>
  <span class="brand__license back__license">#2839165</span>
  <div class="stamp-box"></div>
  <div class="address-line" style="top:164px;"></div>
  <div class="address-line" style="top:215px;"></div>
  <div class="address-line" style="top:268px;"></div>

  <div class="contact-bar">
    <span class="contact-bar__item">
      <svg class="contact-bar__icon" viewBox="0 0 24 24" fill="none" stroke="#fff" stroke-width="1.8"><path d="M5 3h4l2 5-2.5 1.5a11 11 0 0 0 6 6L16 13l5 2v4a2 2 0 0 1-2 2A17 17 0 0 1 3 5a2 2 0 0 1 2-2z"/></svg>
      (323) 555 0148
    </span>
    <span class="contact-bar__item">
      <svg class="contact-bar__icon" viewBox="0 0 24 24" fill="none" stroke="#fff" stroke-width="1.6"><circle cx="12" cy="12" r="10"/><ellipse cx="12" cy="12" rx="4.5" ry="10"/><path d="M2 12h20M4 7h16M4 17h16"/></svg>
      www.bramblecrestworks.com
    </span>
    <span class="contact-bar__item">
      <svg class="contact-bar__icon" viewBox="0 0 24 24" fill="none" stroke="#fff" stroke-width="1.6"><rect x="2" y="5" width="20" height="14"/><path d="M2 5l10 8 10-8"/></svg>
      info@bramblecrestworks.com
    </span>
  </div>
</section>

</body>
</html>
```